Lantern Harbor CD design

I need a CD cover & sleeve design for an upcoming February 2014 CD release event (at a music store). This is a collection of original songs written and sung by yours truly. Many songs are inspired by my ancestors, although there are a few songs that are just about life and love. We are all a product of our ancestry, and we carry this history in our hearts whether we think it influences us or not. This is my first CD although I've been singing and performing for over 30 years, and this body of work is where I'm at now musically and creatively. I'm proud of the effort I've made and want to present myself as someone who is real and genuine. My design style tends towards simple, clean, uncluttered lines, sans serif type faces. No loud or saturated colors please, no reds or pinks. I love the blues & greens. I have a sepia image in my head, but maybe because I've been looking at old photos of my grandparents as inspiration for the last 6 months...!

I am including two shots of me, and some old photos that could be used as a design element, but not mandatory. I wanted you to have some choices... I also have a lot of CD liner notes, but am willing to edit if I need to. This would need to be in 4 color with a sleeve that flaps open, and a lift of something similar for CD imprint. Sorry about the tight deadline, I have to get a print run done before the launch and that lead time is ridiculously tight. If you want an mp3 sample of one song I am happy to forward to give you an idea of my sound, it might help to inspire if you're a music person :-) just let me know at marenvoltatquillmaildotcom

Update for inside text: Cover photo by Arthur Penwick, others photos taken by Maren Volt.

Target Market(s)

Anyone who likes original singer / songwriter music, fellow music lovers, audience members after a performance. My influence is only in the northeast US thus far.

Industry/Entity Type

Store

Requirements
Must have
• Title of CD: Lantern Harbor

Name: Maren Volt

lower left back corner - leave 1-1/4"x1/2" room in design on back cover for UPC barcode
Nice to have
• A lighter touch, artistic vibe, softer painterly approach, Don't mind the blue / green spectrum, or a sepia toned feel. Some music folks feedback has inspired me to update this: I need o have my face on the cover! the b&w shot is a little better. And it would be nice to incorporate both sets of ancestor pictures in some way. (The faded grandma and young boy and the couple with flowers that I am holding).
Song list on the back is helpful, too.
Should not have
• No loud, saturated colors, no reds or pinks please.

```html
<!DOCTYPE html>
<html lang="en">
<head>
<meta charset="utf-8">
<title>Lantern Harbor – CD Packaging</title>
<link rel="stylesheet" href="https://fonts.googleapis.com/css2?family=Montserrat:wght@700&family=Oswald:wght@400&family=Open+Sans:wght@400;600&display=swap">
<style>
  :root{
    --page:#f3f1ec;
    --kraft:#cdb486;
    --kraft-light:#d8c196;
    --kraft-edge:#7a5a2a;
    --spine:#d4bd86;
    --ink-white:#ffffff;
    --photo-sepia-a:#b98e4c;
    --photo-sepia-b:#e6d3a9;
    --photo-grey-a:#4c4d44;
    --photo-grey-b:#8f8a72;
    --disc:#d7bd8a;
  }
  *{box-sizing:border-box;margin:0;padding:0}
  html,body{width:1200px;height:1000px;overflow:hidden;background:var(--page)}
  body{position:relative;font-family:"Open Sans",Arial,sans-serif;color:var(--ink-white)}

  /* Inside spread */
  .spread{position:absolute;left:100px;top:50px;width:1000px;height:500px;display:flex}
  .panel{position:relative;width:490px;height:500px;background:var(--kraft);border-bottom:4px solid var(--kraft-edge);padding:28px 30px}
  .spine{position:relative;width:20px;height:500px;background:var(--spine);border-left:3px solid var(--kraft-edge);border-right:3px solid var(--kraft-edge)}
  .spine-notch{position:absolute;left:-22px;top:215px;width:64px;height:64px;border-radius:50%;background:var(--spine)}
  .liner p{font-size:9.5px;line-height:1.55;margin-bottom:12px;max-width:420px}
  .tracklist{list-style:none;font-size:9.5px;line-height:1.6;margin:10px 0 12px}
  .photo{position:absolute}
  .photo--street{left:30px;right:50px;bottom:26px;height:120px;background:linear-gradient(180deg,var(--photo-sepia-b) 0%,var(--photo-sepia-a) 100%)}
  .photo--garden{left:30px;right:30px;bottom:26px;height:110px;background:linear-gradient(120deg,var(--photo-sepia-b) 0%,var(--photo-sepia-a) 60%,var(--photo-sepia-b) 100%)}

  /* Front cover */
  .cover{position:absolute;left:100px;top:600px;width:360px;height:360px;background:var(--kraft-light);border-bottom:4px solid var(--kraft-edge);overflow:hidden}
  .cover-photo{position:absolute;inset:0;background:
      linear-gradient(135deg,rgba(216,193,150,1) 0%,rgba(143,138,114,.85) 40%,var(--photo-grey-a) 75%,var(--photo-grey-b) 100%)}
  .cover-rule{position:absolute;background:var(--ink-white)}
  .cover-rule--v{left:168px;top:0;width:3px;height:360px}
  .cover-rule--h{left:0;top:172px;width:360px;height:3px}
  .cover-title{position:absolute;left:182px;top:108px;white-space:nowrap}
  .artist{font-family:"Montserrat",Arial,sans-serif;font-weight:700;font-size:28px;line-height:1}
  .album{font-family:"Oswald",Arial,sans-serif;font-weight:400;font-size:19px;letter-spacing:1.5px;text-transform:uppercase;line-height:1.1;margin-top:4px}

  /* Disc */
  .disc{position:absolute;left:700px;top:585px;width:390px;height:390px}
</style>
</head>
<body>

<section class="spread" aria-label="Inside sleeve">
  <div class="panel panel--left liner">
    <p>These songs began on long walks through the towns my family once called home, carrying their stories with me.</p>
    <p>Thank you to everyone who listened, sang along and believed in this music over the years.</p>
    <p>For my grandparents, whose faded photographs kept me company while these songs took shape.</p>
    <p>Recorded and mixed in a small studio by the sea, mastered with care over one winter.</p>
    <div class="photo photo--street" role="img" aria-label="Sepia photograph of an old town street with bare trees"></div>
  </div>

  <div class="spine"><div class="spine-notch"></div></div>

  <div class="panel panel--right liner">
    <p>All songs written and sung by Maren Volt.</p>
    <p>Cover photo by Arthur Penwick. Other photos by Maren Volt.</p>
    <p>Contact marenvoltatquillmaildotcom</p>
    <ol class="tracklist">
      <li>Harbor Light</li>
      <li>Walking Home</li>
      <li>Old Letters</li>
      <li>Winter Field</li>
      <li>Grandmother's Hands</li>
      <li>Salt and Stone</li>
      <li>Quiet Road</li>
      <li>Last Ferry</li>
    </ol>
    <p>© 2014 Maren Volt. All rights reserved.</p>
    <div class="photo photo--garden" role="img" aria-label="Faded sepia photograph of flowers and foliage"></div>
  </div>
</section>

<section class="cover" aria-label="Front cover">
  <div class="cover-photo" role="img" aria-label="Faded portrait of the singer layered with old family photographs of a grandmother and young boy"></div>
  <div class="cover-rule cover-rule--v"></div>
  <div class="cover-rule cover-rule--h"></div>
  <div class="cover-title">
    <h1 class="artist">Maren Volt</h1>
    <div class="album">Lantern Harbor</div>
  </div>
</section>

<svg class="disc" viewBox="0 0 390 390" aria-label="CD disc">
  <circle cx="195" cy="195" r="190" fill="var(--disc)" stroke="#ffffff" stroke-width="6"/>
  <circle cx="195" cy="195" r="58" fill="var(--page)" stroke="#ffffff" stroke-width="6"/>
</svg>

</body>
</html>
```